Kavak Verbatics web design: a translation company with corporate clients

Need a new website for my translation and localization company with file uploading capacity directed to email for quotation

old (very old) web site is www.kvkaktarim.example you can use the content text there or lorem ipsum, We will provide the texts. It will be in English - Turkish - French and German
For the content and overall layout: https://www.pellardlanguages.example/

For the color scheme you'll need to see logo's colors.

I am rebranding so new logo is uploaded The new adress will be www.kavakverbatics.example

Target Market(s)

Primarily corporate clients

Industry/Entity Type

It Company

Coding

Coded - Design and coding required

Number of Pages Required

5+ page

Font styles to use
Other font styles liked:
• Calibri

Requirements
Must have
• References on homepage (logos will be sent during design phase)
• Services: Translation, Interpretation, Localization&Consultancy, Translation API
• Quotation Form and file uploading
• Simple layout evoking reliability, speed and accuracy
Nice to have
• For the content and overall layout: https://www.pellardlanguages.example/
• Separate page for Translation Services: Marketing Translation, Legal Translation, Technical Translation, Personal Translation
• and texts under these headings
Should not have
• Old style
• Complex design

```html
<!DOCTYPE html>
<html lang="en">
<head>
<meta charset="utf-8">
<title>Kavak Verbatics – Translation, Localization &amp; Consultancy</title>
<link href="https://fonts.googleapis.com/css2?family=Raleway:wght@300;400;500;600;700&display=swap" rel="stylesheet">
<style>
:root{
  --orange:#e0912f;
  --orange-dark:#c97d22;
  --ink:#3a3a3a;
  --muted:#777;
  --light:#f1f1f1;
  --white:#fff;
  --footer:#3b3b3b;
  --footer-bottom:#2f2f2f;
  --hero-dark:#0f2d3c;
  --hero-mid:#2a6478;
}
*{box-sizing:border-box;margin:0;padding:0}
html,body{width:1200px;height:2449px;overflow:hidden}
body{font-family:"Raleway",Arial,sans-serif;color:var(--ink);background:var(--white);position:relative}
.header{position:absolute;top:0;left:0;width:1200px;height:122px;background:var(--white);border-top:3px solid var(--orange)}
.brand{position:absolute;left:98px;top:38px;display:flex;align-items:center;gap:12px}
.brand-dot{width:22px;height:22px;border-radius:50%;background:var(--orange)}
.brand-name{font-size:30px;font-weight:500;color:var(--orange);letter-spacing:.5px}
.brand-tag{position:absolute;left:98px;top:80px;font-size:9px;color:var(--muted);letter-spacing:.6px}
.lang{position:absolute;left:911px;top:48px;font-size:12px;color:#7a6a2a;display:flex;align-items:center;gap:10px}
.lang-select{border:1px solid #bbb;border-radius:3px;padding:3px 8px;font-size:10px;color:#333;background:#fafafa}

.hero{position:absolute;top:122px;left:0;width:1200px;height:564px;background:radial-gradient(ellipse at 45% 55%,var(--hero-mid),var(--hero-dark) 70%)}
.nav{position:absolute;top:48px;left:98px;width:1002px;height:44px;background:var(--white);display:flex;align-items:center;border-top:3px solid var(--orange)}
.nav a{font-size:11px;font-weight:600;color:#333;text-decoration:none;flex:1;text-align:center;letter-spacing:.3px}
.nav a.active{flex:0 0 122px;height:44px;margin-top:-3px;background:var(--orange);color:var(--white);display:flex;align-items:center;justify-content:center}
.hero-title{position:absolute;top:230px;left:0;width:1200px;text-align:center;font-size:44px;font-weight:400;color:var(--white);line-height:62px;letter-spacing:.5px}
.dots{position:absolute;top:510px;left:578px;display:flex;gap:6px}
.dots span{width:11px;height:11px;border-radius:50%;background:var(--white)}
.dots span.on{background:var(--orange)}
.hero-arrow{position:absolute;top:686px;left:588px;width:0;height:0;border-left:12px solid transparent;border-right:12px solid transparent;border-top:14px solid var(--hero-dark)}

.section-title{text-align:center;font-size:22px;font-weight:500;color:var(--ink)}
.section-title em{font-style:normal;color:var(--orange);font-weight:400}

.welcome{position:absolute;top:686px;left:0;width:1200px;height:242px}
.welcome .section-title{margin-top:52px}
.welcome .lead{text-align:center;font-size:13px;margin-top:16px;color:#333}
.welcome .body{width:1010px;margin:14px auto 0;text-align:center;font-size:11px;line-height:26px;color:var(--muted)}

.offer{position:absolute;top:928px;left:0;width:1200px;height:378px;background:linear-gradient(180deg,#d59a4e,#c98a3c)}
.offer-row{position:absolute;top:55px;left:101px;display:flex}
.offer-card{width:250px}
.offer-photo{height:188px}
.offer-label{height:82px;background:var(--orange);color:var(--white);font-size:18px;display:flex;align-items:center;justify-content:center;letter-spacing:.3px}
.offer-card:nth-child(2) .offer-label{background:var(--orange-dark)}
.offer-nav{position:absolute;top:176px;width:22px;height:22px;border-radius:50%;background:rgba(255,255,255,.25)}

.partners{position:absolute;top:1306px;left:0;width:1200px;height:270px}
.partners .section-title{margin-top:55px}
.partner-row{position:absolute;top:118px;left:98px;display:flex;gap:30px}
.partner{width:176px;height:104px;border:1px solid #e2e2e2;box-shadow:0 2px 6px rgba(0,0,0,.08);display:flex;align-items:center;justify-content:center}
.partner span{width:110px;height:36px;border-radius:4px;background:#d8dde3}
.partner-arrow{position:absolute;top:158px}

.services{position:absolute;top:1576px;left:0;width:1200px;height:395px;background:var(--light)}
.services .section-title{margin-top:54px}
.service{position:absolute;top:130px;width:240px;text-align:center}
.service-icon{display:block;margin:0 auto;width:90px;height:90px}
.service h3{margin-top:34px;font-size:14px;font-weight:500;color:var(--ink)}
.service h3.hl{color:var(--orange)}
.service p{margin:12px auto 0;width:230px;font-size:12px;line-height:26px;color:var(--muted);white-space:nowrap}

.testimonial{position:absolute;top:1971px;left:0;width:1200px;height:212px}
.avatar{position:absolute;left:101px;top:44px;width:118px;height:118px;border-radius:50%;background:radial-gradient(circle,#e9e2dc,#b8b2ad)}
.quote{position:absolute;left:271px;top:56px;width:800px;font-size:11px;line-height:24px;color:var(--muted);white-space:nowrap}
.qmark{position:absolute;font-size:32px;color:#ccc;font-family:Georgia,serif}
.author{position:absolute;left:271px;top:146px;font-size:10px;color:var(--orange);letter-spacing:.4px}
.role{position:absolute;left:271px;top:166px;font-size:11px;color:var(--muted)}

.footer{position:absolute;top:2183px;left:0;width:1200px;height:217px;background:var(--footer);color:#bbb}
.footer .brand{left:101px;top:76px}
.footer .brand-name{color:#6f5a3a;font-size:28px}
.footer .brand-dot{background:#6f5a3a}
.footer .brand-tag{left:101px;top:118px;color:#6f5a3a}
.footer h4{position:absolute;top:40px;font-size:12px;font-weight:700;color:var(--white);letter-spacing:.4px}
.footer-links{position:absolute;left:381px;top:72px;list-style:none;font-size:11px;line-height:25px;color:#aaa}
.newsletter{position:absolute;left:534px;top:70px;font-size:11px;color:#aaa}
.newsletter .field{margin-top:18px;width:235px;height:32px;background:var(--white);border-radius:2px;color:#777;font-size:11px;padding:9px 12px}
.newsletter .btn{margin-top:14px;width:140px;height:30px;background:var(--orange);color:var(--white);font-size:10px;font-weight:600;display:flex;align-items:center;justify-content:center;border-radius:2px}
.contact{position:absolute;left:836px;top:72px;width:270px;font-size:11px;line-height:22px;color:#aaa}
.contact li{list-style:none;display:flex;gap:12px;margin-bottom:8px}
.contact svg{flex:0 0 12px;margin-top:5px}
.footer-bottom{position:absolute;top:2400px;left:0;width:1200px;height:49px;background:var(--footer-bottom);font-size:11px;color:#999}
.footer-bottom p{position:absolute;left:100px;top:17px}
.footer-bottom a{color:var(--orange)}
.social{position:absolute;left:1016px;top:12px;display:flex;gap:10px}
.social span{width:24px;height:24px;border-radius:50%;background:#555}
</style>
</head>
<body>

<header class="header">
  <div class="brand"><span class="brand-dot"></span><span class="brand-name">Kavak Verbatics</span></div>
  <div class="brand-tag">TRANSLATION, LOCALIZATION &amp; CONSULTANCY</div>
  <div class="lang">Select Language : <span class="lang-select">English ▾</span></div>
</header>

<section class="hero" role="img" aria-label="Business person in a suit behind glowing world globes and a compass rose">
  <nav class="nav">
    <a class="active" href="#">HOME</a>
    <a href="#">OUR SERVICES</a>
    <a href="#">ONLINE TRANSLATION</a>
    <a href="#">GRAPHICS DESIGN</a>
    <a href="#">REFERENCES</a>
    <a href="#">CONTACT US</a>
  </nav>
  <h1 class="hero-title">DELIVERY ON TIME WITH<br>PERFECT QUALITY</h1>
  <div class="dots"><span></span><span class="on"></span><span></span></div>
</section>
<div class="hero-arrow"></div>

<section class="welcome">
  <h2 class="section-title"><em>WELCOME TO</em> KAVAK VERBATICS</h2>
  <p class="lead">KVK Translation Services meets the requirements of various organizations working in legal, finance, marketing and advertisement</p>
  <p class="body">Translated documents are delivered in the required format. Our motto is "Delivery on Time with Perfect Quality". Our translation staff consists of language specialists who are all experts in their fields. By implementing the most appropriate visual ideas, we develop designing and printing stages of all kinds of corporate identity, advertisement, publicity and marketing documents which will raise awareness and serve the branding process.</p>
</section>

<section class="offer">
  <span class="offer-nav" style="left:22px"></span>
  <span class="offer-nav" style="left:1156px"></span>
  <div class="offer-row">
    <div class="offer-card"><div class="offer-photo" role="img" aria-label="Business people meeting at a table" style="background:linear-gradient(160deg,#9fb2c4,#4a5866)"></div><div class="offer-label">TRANSLATION</div></div>
    <div class="offer-card"><div class="offer-photo" role="img" aria-label="Hand writing with a pen" style="background:linear-gradient(160deg,#e4e0dc,#a9a39d)"></div><div class="offer-label">INTERPRETATION</div></div>
    <div class="offer-card"><div class="offer-photo" role="img" aria-label="Close-up of a calculator keypad" style="background:linear-gradient(160deg,#8c8c8c,#3d3d3d)"></div><div class="offer-label">LOCALIZATION</div></div>
    <div class="offer-card"><div class="offer-photo" role="img" aria-label="Globe of flags on a laptop keyboard" style="background:linear-gradient(160deg,#c9ccd6,#6f7583)"></div><div class="offer-label">TRANSLATION API</div></div>
  </div>
</section>

<section class="partners">
  <h2 class="section-title"><em>OUR</em> PARTNERS</h2>
  <svg class="partner-arrow" style="left:38px" width="16" height="30" viewBox="0 0 16 30"><path d="M14 2 2 15l12 13" fill="none" stroke="#ddd" stroke-width="3"/></svg>
  <div class="partner-row">
    <div class="partner"><span></span></div>
    <div class="partner"><span></span></div>
    <div class="partner"><span></span></div>
    <div class="partner"><span></span></div>
    <div class="partner"><span></span></div>
  </div>
  <svg class="partner-arrow" style="left:1146px" width="16" height="30" viewBox="0 0 16 30"><path d="M2 2l12 13L2 28" fill="none" stroke="#ddd" stroke-width="3"/></svg>
</section>

<section class="services">
  <h2 class="section-title"><em>OUR</em> SERVICES</h2>
  <div class="service" style="left:94px">
    <svg class="service-icon" viewBox="0 0 90 90"><circle cx="45" cy="45" r="40" fill="none" stroke="var(--orange)" stroke-width="2"/><path d="M37 32h12l6 6v20H37z" fill="var(--orange)"/></svg>
    <h3 class="hl">MARKETING TRANSLATION</h3>
    <p>Our verbal translators give you simultnous<br>and consecutive interpretation services<br>in all types of business meetings.</p>
  </div>
  <div class="service" style="left:352px">
    <svg class="service-icon" viewBox="0 0 90 90"><circle cx="45" cy="45" r="40" fill="none" stroke="#999" stroke-width="2"/><circle cx="45" cy="45" r="8" fill="none" stroke="#555" stroke-width="5"/></svg>
    <h3>LEGAL TRANSLATION</h3>
    <p>Our verbal translators give you simultnous<br>and consecutive interpretation services<br>in all types of business meetings.</p>
  </div>
  <div class="service" style="left:608px">
    <svg class="service-icon" viewBox="0 0 90 90"><circle cx="45" cy="45" r="40" fill="none" stroke="#999" stroke-width="2"/><path d="M36 50l-4-4 8-8 4 4M54 40l4 4-8 8-4-4M40 50l10-10" fill="none" stroke="#555" stroke-width="3"/></svg>
    <h3>TECHNICAL TRANSLATION</h3>
    <p>Our verbal translators give you simultnous<br>and consecutive interpretation services<br>in all types of business meetings.</p>
  </div>
  <div class="service" style="left:865px">
    <svg class="service-icon" viewBox="0 0 90 90"><circle cx="45" cy="45" r="40" fill="none" stroke="#999" stroke-width="2"/><circle cx="41" cy="48" r="6" fill="none" stroke="#555" stroke-width="4"/><circle cx="53" cy="38" r="4" fill="none" stroke="#555" stroke-width="3"/></svg>
    <h3>PERSONAL TRANSLATION</h3>
    <p>Our verbal translators give you simultnous<br>and consecutive interpretation services<br>in all types of business meetings.</p>
  </div>
</section>

<section class="testimonial">
  <div class="avatar" role="img" aria-label="Portrait of the client giving the testimonial"></div>
  <span class="qmark" style="left:248px;top:38px">“</span>
  <p class="quote">You should know that you have designed a very robust and adaptable system, when we started discussing our needs turnover and volumes were around<br>half of what we are handling today. I don't think any of us envisaged the expansion we have experienced and the system has taken it in its stride,<br>well done to you...</p>
  <span class="qmark" style="left:1034px;top:92px">”</span>
  <div class="author">MASON KELLER</div>
  <div class="role">Marketing Executive</div>
</section>

<footer class="footer">
  <div class="brand"><span class="brand-dot"></span><span class="brand-name">Kavak Verbatics</span></div>
  <div class="brand-tag">TRANSLATION, LOCALIZATION &amp; CONSULTANCY</div>
  <h4 style="left:381px">WELCOME</h4>
  <ul class="footer-links">
    <li>Main Page</li><li>Our Services</li><li>Online Translation</li><li>Graphics Design</li><li>Contact Us</li>
  </ul>
  <h4 style="left:534px">NEWSLETTER</h4>
  <div class="newsletter">
    Get our recent updates through your email id
    <div class="field">Enter your email id</div>
    <div class="btn">SUBSCRIBE NOW</div>
  </div>
  <h4 style="left:834px">CONTACT US</h4>
  <ul class="contact">
    <li><svg width="12" height="14" viewBox="0 0 12 14"><path d="M6 0a5 5 0 0 1 5 5c0 4-5 9-5 9S1 9 1 5a5 5 0 0 1 5-5z" fill="#999"/><circle cx="6" cy="5" r="2" fill="var(--footer)"/></svg><span>Ardıç Sok. Lale Apt. No. 12 Daire 3 Kuzeytepe, 34400 Merkez-İstanbul</span></li>
    <li><svg width="12" height="12" viewBox="0 0 12 12"><path d="M2 0l3 3-1.5 2A7 7 0 0 0 7 8.5L9 7l3 3-2 2C5 12 0 7 0 2z" fill="#999"/></svg><span>Tel-Faks : 0 212 555 0148 - 0 532 555 0193</span></li>
    <li><svg width="12" height="10" viewBox="0 0 12 10"><rect width="12" height="10" fill="#999"/><path d="M0 0l6 5 6-5" fill="none" stroke="var(--footer)"/></svg><span>Email: info@kvkaktarim.example</span></li>
  </ul>
</footer>
<div class="footer-bottom">
  <p>Copyrights 2016. <a>Kavak Verbatics</a>. All rights reserved.</p>
  <div class="social"><span></span><span></span><span></span></div>
</div>

</body>
</html>
```